Business card design needed

Our modern electrical contracting company requires business card design utilising our logo and incorporating our tag line "Service when you need it". We specialise in assisting our customers 24/7 offering a breakdown service.

Industry/Entity Type

Electrical

Contact Information for Business Card

Marcus Penhale, Electrical contractor,Tel: (08) 8456 3071, Fax: (08) 8679 4315, Mob 0438 562 740, Email: marcus.penhale@brightwirepower.com.au, Web: www.brightwirepower.com.au

Requirements
Must have
• we require a 2 sided card.
Front- Logo, tag line and contact information.
Rear- service when you need it! Call now for our 24/7 breakdown service

```html
<!DOCTYPE html>
<html lang="en">
<head>
<meta charset="utf-8">
<title>Breakdown Service Card – Rear</title>
<link rel="stylesheet" href="https://fonts.googleapis.com/css2?family=Carlito:wght@700&family=PT+Sans+Narrow:wght@700&display=swap">
<style>
  :root {
    --card-bg: #e096f9;
    --card-glow: #ffeaff;
    --card-edge: #d9e66e;
    --ink: #141414;
    --disc-light: rgba(255, 240, 255, 0.55);
    --disc-dark: rgba(205, 140, 235, 0.35);
  }
  html, body {
    margin: 0;
    padding: 0;
    width: 1200px;
    height: 741px;
    overflow: hidden;
    background: var(--card-bg);
  }
  .card-rear {
    position: relative;
    width: 1200px;
    height: 741px;
    box-sizing: border-box;
    border: 2px solid var(--card-edge);
    background: radial-gradient(ellipse 46% 48% at 50% 49%, var(--card-glow) 0%, #f5c8fd 35%, var(--card-bg) 100%);
    overflow: hidden;
  }
  .card-rear__disc {
    position: absolute;
    left: 238px;
    top: 11px;
    width: 724px;
    height: 724px;
  }
  .message,
  .message__reflection {
    position: absolute;
    left: 0;
    width: 100%;
    text-align: center;
    color: var(--ink);
    margin: 0;
    line-height: 1;
    white-space: nowrap;
  }
  .message--tagline,
  .message__reflection--tagline {
    left: -4px;
    font-family: "Carlito", "Calibri", sans-serif;
    font-weight: 700;
    font-size: 65px;
    letter-spacing: 0.5px;
  }
  .message--call,
  .message__reflection--call {
    font-family: "PT Sans Narrow", "Arial Narrow", sans-serif;
    font-weight: 700;
    font-size: 70px;
  }
  .message--tagline { top: 236px; }
  .message--call { top: 354px; }
  .message__reflection {
    transform: scaleY(-1);
    opacity: 0.55;
    -webkit-mask-image: linear-gradient(to top, rgba(0,0,0,0.6) 0%, rgba(0,0,0,0) 45%);
    mask-image: linear-gradient(to top, rgba(0,0,0,0.6) 0%, rgba(0,0,0,0) 45%);
  }
  .message__reflection--tagline { top: 291px; }
  .message__reflection--call { top: 414px; }
</style>
</head>
<body>
  <main class="card-rear">
    <svg class="card-rear__disc" viewBox="0 0 724 724" aria-hidden="true">
      <defs>
        <radialGradient id="disc-shade" cx="45%" cy="40%" r="60%">
          <stop offset="0%" stop-color="var(--disc-light)"/>
          <stop offset="100%" stop-color="var(--disc-dark)"/>
        </radialGradient>
      </defs>
      <circle cx="362" cy="362" r="360" fill="url(#disc-shade)"/>
    </svg>

    <h1 class="message message--tagline">Real- service When You Need It!</h1>
    <div class="message__reflection message__reflection--tagline" aria-hidden="true">Real- service When You Need It!</div>

    <p class="message message--call">Call Now For Our 24/7 Breakdown Service</p>
    <div class="message__reflection message__reflection--call" aria-hidden="true">Call Now For Our 24/7 Breakdown Service</div>
  </main>
</body>
</html>
```